We operate a niche online Job Board in Australia. The website is called 'Harvest Roles Australia' and is used by Christian Employers to advertise their job vacancies.
I would like a business card that identifies with our website (www.harvestroles-example.com.au). We would like the same colors and fonts used on our business card from our website. When people look at our business card we want them to be able to recognise it from the website.
We want the web address to be dominant.
Updates
We are liking those that use white space as well as the blue and orange and those that highlight the url.
We now have 60 designs and therefore will not wait for the Sunday deadline to make a decision. We have a few we like.
The ones we like are:
- bold
- creative
- colorful (blue orange and white)
- some white space
- no boxes or borders
- font the same as our website
- reflects the look of our website
We will make a final decision in the next 6 hours so please if you think you have something to offer then get it in within the next 6 hours. If you think you will leave it till later you will miss out. Thanks to all those who have responded with some great designs, sorry we can't reward all of you!
Industry/Entity Type
Business
Contact Information for Business Card
Harvest Roles Australia
www.harvestroles-example.com.au
Peter Galvridge
CEO
Phone: 1300 512 874
Mobile: 0412 735019
Fax: (03) 9157 2360
email: peter@harvestroles-example.com.au
Requirements
Should not have
- We do not want a cross or any cliche christian images.

```html
<!DOCTYPE html>
<html lang="en">
<head>
<meta charset="utf-8">
<title>Harvest Roles Australia – Business Card</title>
<link rel="stylesheet" href="https://fonts.googleapis.com/css2?family=Crimson+Text:wght@600;700&family=Open+Sans:wght@400;600&display=swap">
<style>
  :root {
    --navy: #27215f;
    --orange: #f7941d;
    --paper: #ffffff;
    --backdrop: #9a9a9c;
    --rule: #9d9d9d;
    --ink: #222222;
  }
  * { margin: 0; padding: 0; box-sizing: border-box; }
  html, body { width: 900px; height: 1200px; overflow: hidden; }
  body {
    background: var(--backdrop);
    display: flex; align-items: center; justify-content: center;
  }
  .business-card {
    position: relative;
    width: 760px; height: 420px;
    background: var(--paper);
    box-shadow: 0 10px 30px rgba(0,0,0,0.25);
  }
  .card-edges { position: absolute; inset: 0; }
  .brand-side {
    position: absolute; left: 0; top: 0; width: 380px; height: 100%;
    display: flex; align-items: center; justify-content: center;
  }
  .brand-name {
    font-family: "Crimson Text", Georgia, serif;
    font-weight: 700; font-size: 36px; color: var(--navy);
    letter-spacing: -0.3px; line-height: 1.05; text-align: center;
  }
  .divider {
    position: absolute; left: 380px; top: 70px; width: 1px; height: 260px;
    background: var(--rule);
  }
  .person-side { position: absolute; left: 400px; top: 0; width: 330px; height: 100%; }
  .person-name, .person-role {
    font-family: "Crimson Text", Georgia, serif; font-weight: 700;
    color: var(--ink); text-align: center;
  }
  .person-name { margin-top: 78px; font-size: 27px; line-height: 1.1; }
  .person-role { font-size: 25px; line-height: 1.1; }
  .contact-list { list-style: none; margin-top: 58px; margin-left: 12px; }
  .contact-item {
    display: flex; align-items: center; height: 27px;
    font-family: "Open Sans", Arial, sans-serif; font-size: 13px; color: var(--ink);
  }
  .contact-icon { width: 18px; height: 18px; margin-right: 10px; flex: none; }
  .contact-label { width: 62px; }
</style>
</head>
<body>
  <div class="business-card">
    <svg class="card-edges" width="760" height="420" viewBox="0 0 760 420" aria-hidden="true">
      <!-- top band -->
      <path d="M0 0 H310 Q300 12 290 12 H0 Z" fill="var(--orange)"/>
      <path d="M296 0 H760 V20 H330 Q318 20 312 10 Q306 0 296 0 Z" fill="var(--navy)"/>
      <!-- bottom band -->
      <path d="M0 406 H540 Q552 406 558 414 Q564 420 575 420 H0 Z" fill="var(--navy)"/>
      <path d="M560 420 Q566 400 585 400 H760 V420 Z" fill="var(--orange)"/>
      <!-- side tabs -->
      <path d="M760 110 H752 Q744 110 744 120 V300 Q744 312 752 312 H760 Z" fill="var(--orange)"/>
      <path d="M0 110 H6 Q14 110 14 120 V300 Q14 312 6 312 H0 Z" fill="var(--navy)"/>
    </svg>

    <div class="brand-side">
      <p class="brand-name">Harvest Roles<br>Australia</p>
    </div>

    <div class="divider"></div>

    <div class="person-side">
      <p class="person-name">Peter Galvridge</p>
      <p class="person-role">CEO</p>
      <ul class="contact-list">
        <li class="contact-item">
          <svg class="contact-icon" viewBox="0 0 18 18"><circle cx="9" cy="9" r="9" fill="var(--navy)"/><rect x="4.5" y="5.5" width="9" height="7" fill="none" stroke="#fff" stroke-width="1.2"/><path d="M4.5 5.5 L9 9.5 L13.5 5.5" fill="none" stroke="#fff" stroke-width="1.2"/></svg>
          <span class="contact-label">Email</span><span>: peter@harvestroles-example.com.au</span>
        </li>
        <li class="contact-item">
          <svg class="contact-icon" viewBox="0 0 18 18"><circle cx="9" cy="9" r="9" fill="var(--navy)"/><path d="M6 4.5 Q4 6 5.5 9.5 Q7.5 13 11.5 13.5 L12.8 11.8 L10.8 10.5 L9.8 11.3 Q7.5 10 6.9 7.9 L7.8 7 L7 4.8 Z" fill="#fff"/></svg>
          <span class="contact-label">Phone</span><span>: 1300 512 874</span>
        </li>
        <li class="contact-item">
          <svg class="contact-icon" viewBox="0 0 18 18"><circle cx="9" cy="9" r="9" fill="var(--navy)"/><rect x="6.2" y="4" width="5.6" height="10" rx="1" fill="#fff"/><rect x="7.2" y="5.2" width="3.6" height="6" fill="var(--navy)"/></svg>
          <span class="contact-label">Mobile</span><span>: 0412 735019</span>
        </li>
        <li class="contact-item">
          <svg class="contact-icon" viewBox="0 0 18 18"><circle cx="9" cy="9" r="9" fill="var(--navy)"/><rect x="6" y="4" width="6" height="4" fill="#fff"/><rect x="4" y="8" width="10" height="5" rx="1" fill="#fff"/><rect x="6.5" y="10" width="5" height="1" fill="var(--navy)"/></svg>
          <span class="contact-label">Fax</span><span>: (03) 9157 2360</span>
        </li>
        <li class="contact-item">
          <svg class="contact-icon" viewBox="0 0 18 18"><circle cx="9" cy="9" r="9" fill="var(--navy)"/><circle cx="9" cy="9" r="4.8" fill="none" stroke="#fff" stroke-width="1.1"/><ellipse cx="9" cy="9" rx="2" ry="4.8" fill="none" stroke="#fff" stroke-width="1"/><path d="M4.2 9 H13.8" stroke="#fff" stroke-width="1"/></svg>
          <span class="contact-label">Website</span><span>: www.harvestroles-example.com.au</span>
        </li>
      </ul>
    </div>
  </div>
</body>
</html>
```